Retail healthy snack bar design

We are launching a new product range to be sold in health food stores.

The Vorla Co (no logo as yet).

We will have a range of bars, spreads (jars), shakes (bags) in the following ranges-
milk protein
plant protein
keto

For this project, please do a bar design. The chosen designer will be given additional work for the rest of the packaging as well as promotional material such as social media, banners, posters etc.

Brisk Stick Protein - Must be White to be recognized.
Brisk Stick Collagen - Bronze
Brisk Keto Stick - Possibly Red
Brisk Stick Plant - Green

Food images can be added but their must be samples without as we may need to remove for certain countries.

Target Market(s)

Healthy, Weight-loss, Bodybuilding, Elderly, Medical

Industry/Entity Type

Health And Wellness

Font styles to use
Sans Serif

Colors

Designer to choose colors to be used in the design.

Requirements
Must have
• Clean simple to read design with minimal colours

Flavour to be easily read (Must include the word 'Flavour' in the same size font as the flavour description)

Must show size of bar (60g).

Some details that can be added (optional)-
raw, cold pressed bar with (example) whey protein isolate + prebiotic fibre
natural, with no artificial colours, flavours, preservatives or sweeteners
no added sugar or sugar alcohols - gluten free - soy free

Rear of bar shall remain the same or all same details if redesigned.
Nice to have
• Clean design, use of silver foil and/or matt/gloss affect, large oversized flavour image (if including).

See images of current designs I like on the market for ideas
Should not have
• Too many images (if any).

```html
<!DOCTYPE html>
<html lang="en">
<head>
<meta charset="utf-8">
<title>The Vorla Co – Brisk Stick Range</title>
<link rel="stylesheet" href="https://fonts.googleapis.com/css2?family=Roboto+Condensed:wght@300;400;700;800&family=Teko:wght@500&family=Open+Sans:wght@400&family=Ubuntu:wght@500&family=Poppins:wght@300&display=swap">
<style>
  :root{
    --canvas:#bdbdbd;
    --wrap-black:#232222;
    --wrap-black-hi:#3a3939;
    --gold-dark:#8a5a1c;
    --gold-light:#f3d27a;
    --ink:#1f1d1d;
    --white:#ffffff;
    --protein-accent:#b3262e;
    --collagen-accent:#8b4a22;
    --keto-accent:#a82a24;
    --plant-accent:#2d9a4c;
  }
  *{box-sizing:border-box;margin:0;padding:0}
  html,body{width:1200px;height:2256px;overflow:hidden}
  body{
    background:linear-gradient(180deg,#b3b3b3 0%,#c4c4c4 50%,#b8b8b8 100%);
    position:relative;
    font-family:"Roboto Condensed",sans-serif;
  }
  .wrapper{
    position:absolute;left:85px;width:1032px;height:410px;
    background:var(--wrap-black);
    box-shadow:0 6px 14px rgba(0,0,0,.25);
  }
  .wrapper--protein{top:155px;--accent:var(--protein-accent);--front:linear-gradient(180deg,#f2f2f2 0%,#fff 8%,#fff 92%,#e6e6e6 100%);--band:#d9d9de;--tag:#2a2a2a;--divider:var(--protein-accent)}
  .wrapper--collagen{top:655px;--accent:var(--collagen-accent);--front:linear-gradient(180deg,#d3792e 0%,#de9a3c 60%,#e8b04c 100%);--band:#9a5a22;--tag:#5a3014;--divider:#8b4a22}
  .wrapper--keto{top:1169px;--accent:var(--keto-accent);--front:linear-gradient(180deg,#d4372a 0%,#e2432f 60%,#e9503f 100%);--band:#a62a22;--tag:#8a2019;--divider:#a82a24}
  .wrapper--plant{top:1690px;--accent:var(--plant-accent);--front:linear-gradient(180deg,#86bf48 0%,#98ca52 60%,#acd66c 100%);--band:#6a9a3c;--tag:#2e6a30;--divider:#2d9a4c}

  .crimp{position:absolute;top:0;width:6px;height:410px}
  .crimp--left{left:0}
  .crimp--right{right:0}

  .end-seal{position:absolute;top:0;height:410px;
    background:linear-gradient(90deg,var(--wrap-black) 0%,var(--wrap-black-hi) 45%,#5a5858 58%,var(--wrap-black-hi) 70%,var(--wrap-black) 100%)}
  .end-seal--left{left:6px;width:80px}
  .end-seal--right{left:920px;width:106px;
    background:linear-gradient(90deg,var(--wrap-black) 0%,#2e2d2d 40%,#3d3c3c 55%,var(--wrap-black) 100%)}

  .gold-stripe{position:absolute;top:0;height:410px;
    background:linear-gradient(180deg,var(--gold-dark) 0%,var(--gold-light) 35%,#c4913a 60%,var(--gold-light) 85%,var(--gold-dark) 100%)}
  .gold-stripe--left{left:86px;width:10px}
  .gold-stripe--right{left:672px;width:12px}
  .edge-band{position:absolute;left:96px;top:0;width:23px;height:410px;background:var(--band)}

  .front{position:absolute;left:119px;top:0;width:553px;height:410px;background:var(--front);overflow:hidden}
  .front-curve{position:absolute;inset:0}

  .brand-pill{position:absolute;left:0;top:93px;width:190px;height:31px;background:var(--accent);
    border-radius:0 16px 16px 0;color:var(--white);font-family:"Ubuntu",sans-serif;font-weight:500;font-size:21px;
    line-height:31px;padding-left:36px;white-space:nowrap}
  .line-name{position:absolute;left:279px;top:85px;font-family:"Poppins",sans-serif;font-weight:300;font-size:37px;
    letter-spacing:9px;color:var(--ink);line-height:44px}
  .weight{position:absolute;left:466px;top:84px;font-family:"Roboto Condensed",sans-serif;font-weight:700;font-size:44px;
    color:var(--ink);line-height:46px;letter-spacing:-1px}
  .product-title{position:absolute;left:43px;top:150px;width:470px;font-size:68px;line-height:74px;color:var(--ink);white-space:nowrap;
    display:flex;justify-content:space-between;letter-spacing:-1px}
  .product-title b{font-weight:800}
  .product-title span{font-weight:400}
  .product-title--spaced{font-size:66px;letter-spacing:0}
  .product-title--spaced b{letter-spacing:10px}
  .product-title--spaced span{letter-spacing:8px;margin-right:-8px}
  .flavour{position:absolute;left:44px;top:232px;width:469px;height:49px;background:var(--accent);color:var(--white);
    font-family:"Teko",sans-serif;font-weight:500;font-size:41px;line-height:54px;text-align:center;letter-spacing:1.6px;white-space:nowrap;overflow:hidden}
  .tagline{position:absolute;left:44px;top:297px;width:470px;font-family:"Open Sans",sans-serif;font-size:21px;letter-spacing:1.4px;
    color:var(--tag);display:flex;justify-content:space-between;align-items:center;white-space:nowrap}
  .tagline i{display:inline-block;width:2px;height:28px;background:var(--divider)}

  .back{position:absolute;left:684px;top:0;width:236px;height:410px}
  .claims{position:absolute;left:18px;top:100px;list-style:none;color:#f2f2f2;font-family:"Roboto Condensed",sans-serif;
    font-weight:300;font-size:18.5px;line-height:21px}
  .claims li{position:relative;padding-left:14px}
  .claims li::before{content:"";position:absolute;left:0;top:7px;width:8px;height:8px;border-radius:50%;background:var(--dot)}
  .wrapper--protein .claims{--dot:#c4303a}
  .wrapper--collagen .claims{--dot:#e8923a}
  .wrapper--keto .claims{--dot:#e0453a}
  .wrapper--plant .claims{--dot:#8cc84a}
</style>
</head>
<body>

<svg width="0" height="0" style="position:absolute" aria-hidden="true">
  <defs>
    <pattern id="crimp-teeth-left" width="6" height="8" patternUnits="userSpaceOnUse">
      <polygon points="0,0 6,0 0,4 6,8 0,8" fill="#bbbbbb"/>
    </pattern>
    <pattern id="crimp-teeth-right" width="6" height="8" patternUnits="userSpaceOnUse">
      <polygon points="6,0 0,0 6,4 0,8 6,8" fill="#bbbbbb"/>
    </pattern>
  </defs>
</svg>

<!-- Protein -->
<section class="wrapper wrapper--protein">
  <div class="end-seal end-seal--left"></div>
  <div class="gold-stripe gold-stripe--left"></div>
  <div class="edge-band"></div>
  <div class="front">
    <div class="brand-pill">The Vorla Co</div>
    <div class="line-name">Brisk</div>
    <div class="weight">60g</div>
    <h2 class="product-title"><b>PROTEIN</b><span>STICK</span></h2>
    <div class="flavour">Peanut Chocolate Chip Flavour</div>
    <p class="tagline">Snack with High Protein <i></i> Super Food Bar</p>
  </div>
  <div class="gold-stripe gold-stripe--right"></div>
  <div class="back">
    <ul class="claims">
      <li>Raw, cold pressed bar<br>whey protein isolate +<br>prebiotic fibre natural</li>
      <li>No artificial colours,<br>flavours, preservatives<br>or sweeteners</li>
      <li>No added sugar or<br>sugar alcohols</li>
      <li>Gluten free</li>
      <li>Soy free</li>
    </ul>
  </div>
  <div class="end-seal end-seal--right"></div>
  <svg class="crimp crimp--left"><rect width="6" height="410" fill="url(#crimp-teeth-left)"/></svg>
  <svg class="crimp crimp--right"><rect width="6" height="410" fill="url(#crimp-teeth-right)"/></svg>
</section>

<!-- Collagen -->
<section class="wrapper wrapper--collagen">
  <div class="end-seal end-seal--left"></div>
  <div class="gold-stripe gold-stripe--left"></div>
  <div class="edge-band"></div>
  <div class="front">
    <svg class="front-curve" width="553" height="410" aria-hidden="true"><path d="M0 410 L0 340 C180 330 380 220 410 0 L553 0 L553 410 Z" fill="#f0be5a" opacity=".35"/></svg>
    <div class="brand-pill">The Vorla Co</div>
    <div class="line-name">Brisk</div>
    <div class="weight">60g</div>
    <h2 class="product-title"><b>COLLAGEN</b><span>STICK</span></h2>
    <div class="flavour">Peanut Chocolate Chip Flavour</div>
    <p class="tagline">Snack with High Protein <i></i> Super Food Bar</p>
  </div>
  <div class="gold-stripe gold-stripe--right"></div>
  <div class="back">
    <ul class="claims">
      <li>Raw, cold pressed bar<br>whey protein isolate +<br>prebiotic fibre natural</li>
      <li>No artificial colours,<br>flavours, preservatives<br>or sweeteners</li>
      <li>No added sugar or<br>sugar alcohols</li>
      <li>Gluten free</li>
      <li>Soy free</li>
    </ul>
  </div>
  <div class="end-seal end-seal--right"></div>
  <svg class="crimp crimp--left"><rect width="6" height="410" fill="url(#crimp-teeth-left)"/></svg>
  <svg class="crimp crimp--right"><rect width="6" height="410" fill="url(#crimp-teeth-right)"/></svg>
</section>

<!-- Keto -->
<section class="wrapper wrapper--keto">
  <div class="end-seal end-seal--left"></div>
  <div class="gold-stripe gold-stripe--left"></div>
  <div class="edge-band"></div>
  <div class="front">
    <svg class="front-curve" width="553" height="410" aria-hidden="true"><path d="M0 410 L0 345 C180 335 380 225 410 0 L553 0 L553 410 Z" fill="#f06a50" opacity=".3"/></svg>
    <div class="brand-pill">The Vorla Co</div>
    <div class="line-name">Brisk</div>
    <div class="weight">60g</div>
    <h2 class="product-title product-title--spaced"><b>KETO</b><span>STICK</span></h2>
    <div class="flavour">Peanut Chocolate Chip Flavour</div>
    <p class="tagline">Snack with High Protein <i></i> Super Food Bar</p>
  </div>
  <div class="gold-stripe gold-stripe--right"></div>
  <div class="back">
    <ul class="claims">
      <li>Raw, cold pressed bar<br>whey protein isolate +<br>prebiotic fibre natural</li>
      <li>No artificial colours,<br>flavours, preservatives<br>or sweeteners</li>
      <li>No added sugar or<br>sugar alcohols</li>
      <li>Gluten free</li>
      <li>Soy free</li>
    </ul>
  </div>
  <div class="end-seal end-seal--right"></div>
  <svg class="crimp crimp--left"><rect width="6" height="410" fill="url(#crimp-teeth-left)"/></svg>
  <svg class="crimp crimp--right"><rect width="6" height="410" fill="url(#crimp-teeth-right)"/></svg>
</section>

<!-- Plant -->
<section class="wrapper wrapper--plant">
  <div class="end-seal end-seal--left"></div>
  <div class="gold-stripe gold-stripe--left"></div>
  <div class="edge-band"></div>
  <div class="front">
    <svg class="front-curve" width="553" height="410" aria-hidden="true"><path d="M0 410 L0 345 C180 335 380 225 410 0 L553 0 L553 410 Z" fill="#c2e48a" opacity=".35"/></svg>
    <div class="brand-pill">The Vorla Co</div>
    <div class="line-name">Brisk</div>
    <div class="weight">60g</div>
    <h2 class="product-title product-title--spaced"><b>PLANT</b><span>STICK</span></h2>
    <div class="flavour">Peanut Chocolate Chip Flavour</div>
    <p class="tagline">Snack with High Protein <i></i> Super Food Bar</p>
  </div>
  <div class="gold-stripe gold-stripe--right"></div>
  <div class="back">
    <ul class="claims">
      <li>Raw, cold pressed bar<br>whey protein isolate +<br>prebiotic fibre natural</li>
      <li>No artificial colours,<br>flavours, preservatives<br>or sweeteners</li>
      <li>No added sugar or<br>sugar alcohols</li>
      <li>Gluten free</li>
      <li>Soy free</li>
    </ul>
  </div>
  <div class="end-seal end-seal--right"></div>
  <svg class="crimp crimp--left"><rect width="6" height="410" fill="url(#crimp-teeth-left)"/></svg>
  <svg class="crimp crimp--right"><rect width="6" height="410" fill="url(#crimp-teeth-right)"/></svg>
</section>

</body>
</html>
```